Stationary Design to Complement our Website

We would like template designed for word documents that we can use for headed paper. The template should complement the style of our website & incorporate our existing logo. https://www.velmorantravel.com/

The header and footer design should be sperate PNG or JPEG files that we can copy and paste into word header and footers. They should work on A4 & letter sized papers.

Note the main web colours are as follows:

Black
HEX code #2b2c2b
C=71 M=64 Y=64 K=65
RGB 43,44,43

Green
HEX code #116c49
C=88 M=33 Y=82 K=24
RGB 17,108,73

Current fonts are ALEO & Gilroy.

Fonts and colours in new design don't have to match website exactly but should be complementary.

Font styles to use
Serif

Requirements
Must have
• a simple design that complements our website.
Some kind of graphic on the top & some sort of graphic on the bottom. Not just plain logo on top.
designs that incorporate the clouds might look good
Can also incorporate 5* rate harbor rating
Should not have
• no photographs included on the design

```html
<!DOCTYPE html>
<html lang="en">
<head>
<meta charset="utf-8">
<title>Velmoran Travel – Letterhead</title>
<link rel="stylesheet" href="https://fonts.googleapis.com/css2?family=EB+Garamond:ital,wght@0,400;0,500;1,400&family=Outfit:wght@700&display=swap">
<style>
  :root {
    --leaf: #8ca34f;
    --forest: #116c49;
    --ink: #2b2c2b;
    --text-grey: #5e5f5e;
    --paper: #ffffff;
    --sig-fill: #f1f1ef;
  }
  * { margin: 0; padding: 0; box-sizing: border-box; }
  html, body { width: 927px; height: 1200px; overflow: hidden; background: var(--paper); }
  .letterhead {
    position: relative; width: 927px; height: 1200px; overflow: hidden;
    font-family: "EB Garamond", Georgia, serif; color: var(--ink);
  }
  .header-band { position: absolute; left: 0; top: 0; width: 927px; height: 148px; background: var(--leaf); }
  .header-stripe { position: absolute; left: 309px; top: 140px; width: 618px; height: 16px; background: var(--forest); }

  .brand {
    position: absolute; left: 41px; top: 44px; display: flex; align-items: flex-start; gap: 10px;
    color: var(--paper); font-size: 25px; line-height: 31px; letter-spacing: 5px; font-weight: 400;
  }
  .brand-dot { width: 14px; height: 14px; border-radius: 50%; background: var(--paper); margin-top: 2px; }

  .contact { position: absolute; right: 75px; top: 36px; list-style: none; color: var(--paper); }
  .contact li {
    display: flex; justify-content: flex-end; align-items: center; gap: 12px;
    height: 26px; font-size: 16px; letter-spacing: 2.6px;
  }
  .contact svg { width: 15px; height: 15px; fill: var(--paper); flex: none; }

  .recipient { position: absolute; left: 77px; top: 211px; }
  .recipient .label, .recipient .position { font-size: 12.5px; color: var(--text-grey); line-height: 20px; }
  .recipient .name { font-size: 16px; line-height: 20px; }

  .date { position: absolute; right: 80px; top: 229px; font-size: 15px; }

  .company { position: absolute; left: 77px; top: 324px; }
  .company .company-name { font-size: 16px; line-height: 24px; }
  .company .address { font-size: 12.5px; line-height: 20px; color: var(--text-grey); }

  .letter-body { position: absolute; left: 308px; top: 318px; width: 539px; }
  .greeting { font-size: 21px; font-weight: 400; line-height: 30px; }
  .letter-body p {
    font-size: 13.1px; line-height: 20.2px; color: var(--text-grey);
    text-align: justify; margin-bottom: 20px;
  }

  .signature-mark { position: absolute; left: 309px; top: 895px; width: 165px; height: 60px; background: var(--sig-fill); border-radius: 4px; }
  .signer { position: absolute; left: 308px; top: 965px; }
  .signer .signer-name { font-size: 18px; color: var(--text-grey); line-height: 24px; }
  .signer .signer-role { font-size: 12px; font-style: italic; color: var(--text-grey); margin-top: 2px; }

  .footer-band { position: absolute; left: 0; top: 1135px; width: 927px; height: 65px; background: var(--forest); }
  .footer-accent { position: absolute; left: 0; top: 1135px; width: 927px; height: 65px; }
  .tagline {
    position: absolute; left: 23px; top: 1145px;
    font-family: "Outfit", Arial, sans-serif; font-weight: 700; font-size: 31px;
    color: var(--paper); letter-spacing: -0.2px; line-height: 44px;
  }
</style>
</head>
<body>
<main class="letterhead">
  <div class="header-band"></div>
  <div class="header-stripe"></div>

  <div class="brand">
    <span class="brand-dot"></span>
    <span class="brand-name">VELMORAN<br>TRAVEL</span>
  </div>

  <ul class="contact">
    <li>info@velmorantravel.com
      <svg viewBox="0 0 16 16"><path d="M1 3h14v10H1z M1.5 3.5 8 9l6.5-5.5" fill="none" stroke="#fff" stroke-width="1.4"/><path d="M1 3h14L8 8.6z"/></svg>
    </li>
    <li>www.velmorantravel.com
      <svg viewBox="0 0 16 16"><circle cx="8" cy="8" r="6.8" fill="none" stroke="#fff" stroke-width="1.4"/><ellipse cx="8" cy="8" rx="3" ry="6.8" fill="none" stroke="#fff" stroke-width="1.2"/><path d="M1.5 6h13M1.5 10h13" stroke="#fff" stroke-width="1.2"/></svg>
    </li>
    <li>Toll Free +1 877-555-0142
      <svg viewBox="0 0 16 16"><path d="M3.6 1.2 6 3.8 4.8 5.8c.9 2 2.6 3.8 4.6 4.7l2-1.3 2.6 2.4-1.4 2.6C7.3 14 2 8.8 1 3z"/></svg>
    </li>
  </ul>

  <section class="recipient">
    <div class="label">To</div>
    <div class="name">NAME</div>
    <div class="position">Position</div>
  </section>

  <div class="date">3 February 2020</div>

  <section class="company">
    <div class="company-name">Company Name</div>
    <div class="address">123 Street Name city name</div>
    <div class="address">1234 , Country</div>
  </section>

  <article class="letter-body">
    <h1 class="greeting">Hello,</h1>
    <p>Lorem ipsum dolor sit amet, consectetur adipiscing elit. Integer et aliquet risus. Suspendisse mattis justo id velit mollis ullamcorper. Integer fermentum ornare egestas. Nunc facilisis enim id metus tempor, ac auctor velit iaculis. Integer semper rutrum volutpat. Donec ut lacinia tortor. Integer maximus nulla vel ante pretium maximus.</p>
    <p>Vestibulum ante ipsum primis in faucibus orci luctus et ultrices posuere cubilia Curae; Donec lobortis quam ac mi aliquam, sed lacinia ligula cursus. Pellentesque ac velit sed lacus varius volutpat sit amet at sapien. Vivamus nec tempus ante. Donec volutpat diam et nibh lacinia, sit amet pulvinar dui vestibulum. Donec lobortis quam ac mi aliquam, sed lacinia ligula cursus. Fusce eget ipsum id libero facilisis ornare sed blandit sapien. Vestibulum ante ipsum primis in faucibus orci luctus et ultrices posuere cubilia Cura</p>
    <p>Vestibulum ante ipsum primis in faucibus orci luctus et ultrices posuere cubilia Curae; Donec lobortis quam ac mi aliquam, sed lacinia ligula cursus. Pellentesque ac velit sed lacus varius volutpat sit amet at sapien. Vivamus nec tempus ante. Donec volutpat diam et nibh lacinia, sit amet pulvinar dui vestibulum. Fusce eget ipsum id libero facilisis ornare sed blandit sapien. Vestibulum ante ipsum primis in faucibus orci luctus et ultrices posuere cubilia Curae. Nunc a commodo erat.</p>
    <p>In nec egestas purus, vehicula porttitor nunc. Donec faucibus velit nec lobortis hendrerit. Donec volutpat diam et nibh lacinia, sit amet pulvinar dui vestibulum. Fusce eget ipsum id libero facilisis ornare sed blandit sapien. Vestibulum ante ipsum primis in faucibus orci luctus et ultrices posuere cubilia Curae. Nunc a commodo erat. In nec egestas purus.</p>
  </article>

  <div class="signature-mark" role="img" aria-label="Handwritten signature"></div>
  <section class="signer">
    <div class="signer-name">Name ,Surname</div>
    <div class="signer-role">General Manager.</div>
  </section>

  <div class="footer-band"></div>
  <svg class="footer-accent" viewBox="0 0 927 65" aria-hidden="true">
    <polygon points="519,33 927,33 927,65 501,65" fill="#8ca34f"/>
  </svg>
  <div class="tagline">Experience Ireland like a local.</div>
</main>
</body>
</html>
```